Brava Set CEO and Partners Business Card

We need a fresh, fun, simple and clean business card design....we would like a template where we can add a name and title (as well as specific email addresses). We are open to different looks (full logo on one side and a small logo on the company info side, or our logo is in the background but faint on one side but full on the other, or something else cool :-) ). Our colors are in our logo: blue, black and white...however we are not opposed to the use of other colors if it works. We build sets, make props and a host of other things for the film and television industry...our card should reflect creativity, style and professionalism.

A white background would be preferred.

I would like to see an option with Facebook and Instagram icons.

Facebook- facebook.com/bravasetny
Instagram- brava_set

Our website is bravaset-example.com.

Brava Set, Inc.
418 Corvell Avenue, Unit 9
North Hollywood, California 91602
555.210.4873 | tel
555.210.6692 | fax
www.BravaSet-example.com

Sample Name and Title #1:

Peter Halvik
CEO / Co-Owner
555.210.4873 | tel
555.210.6692 | fax
peter@bravaset-example.com
www.BravaSet-example.com

Target Market(s)

Marketing Professionals, Production Designers, Interior Designers, Film Producers, Directors, Art Directors, Event Directors

Industry/Entity Type

Entertainment Industry

Contact Information for Business Card

Peter Halvik
CEO / Co-Owner
555.210.4873 | tel
555.210.6692 | fax
peter@bravaset-example.com
www.BravaSet-example.com

Font styles to use
Sans Serif

Colors
33a6d7
ffffff
1b1b1b

Requirements
Must have
• Logo, All Contact Info, White Background. Symmetry.
Nice to have
• Facebook and Instagram icons with addresses
• Facebook- facebook.com/bravasetny
• Instagram- brava_set

```html
<!DOCTYPE html>
<html lang="en">
<head>
<meta charset="utf-8">
<title>Brava Set – Business Card</title>
<link href="https://fonts.googleapis.com/css2?family=Roboto:wght@400;500;900&display=swap" rel="stylesheet">
<style>
  :root {
    --brand-blue: #33a6d7;
    --brand-black: #1b1b1b;
    --brand-white: #ffffff;
    --text-grey: #5a5a5a;
    --rule-grey: #c9c9c9;
    --backdrop: #d6d6d6;
  }
  * { margin: 0; padding: 0; box-sizing: border-box; }
  html, body {
    width: 1200px; height: 1000px; overflow: hidden;
    background: var(--backdrop);
    font-family: "Roboto", sans-serif;
  }
  .stage { position: relative; width: 1200px; height: 1000px; }

  /* Front side */
  .card-front {
    position: absolute; left: 220px; top: 50px; width: 760px; height: 433px;
    background: linear-gradient(115deg, #000 0%, #050505 52%, #1e1e1e 56%, #2a2a2a 100%);
    box-shadow: 0 6px 14px rgba(0,0,0,.35);
    overflow: hidden;
  }
  .front-wordmark {
    position: absolute; left: 0; right: 0; top: 190px;
    text-align: center; font-weight: 900; font-size: 118px; line-height: 1;
    letter-spacing: -2px; color: var(--brand-white);
  }
  .front-url {
    position: absolute; left: 0; right: 0; top: 380px;
    text-align: center; font-size: 17px; line-height: 22px; font-weight: 500;
    color: var(--brand-white);
  }
  .accent { color: var(--brand-blue); }

  /* Back side */
  .card-back {
    position: absolute; left: 220px; top: 524px; width: 760px; height: 434px;
    background: var(--brand-white); overflow: hidden;
    box-shadow: 0 6px 14px rgba(0,0,0,.35);
  }
  .back-wordmark {
    position: absolute; left: 42px; top: 60px;
    font-weight: 900; font-size: 66px; line-height: 1; letter-spacing: -1px;
    color: var(--brand-black);
  }
  .holder { position: absolute; right: 43px; top: 205px; text-align: right; }
  .holder-name { font-size: 23px; font-weight: 500; color: var(--brand-blue); }
  .holder-title { font-size: 17px; color: var(--text-grey); margin-top: 3px; }
  .divider {
    position: absolute; left: 42px; right: 43px; top: 267px;
    border-top: 1.5px solid var(--rule-grey);
  }
  .contact-list {
    position: absolute; left: 42px; top: 284px; list-style: none;
    font-size: 17px; color: var(--text-grey); line-height: 22px;
  }
  .contact-list li { display: flex; align-items: center; gap: 7px; }
  .contact-list svg { width: 13px; height: 13px; fill: var(--brand-blue); flex: none; }
  .address {
    position: absolute; right: 45px; top: 284px; text-align: right;
    font-size: 17px; color: var(--text-grey); line-height: 22px; font-style: normal;
  }
  .social {
    position: absolute; right: 50px; top: 363px; display: flex; gap: 20px;
    font-size: 17px; color: var(--text-grey);
  }
  .social span { display: flex; align-items: center; gap: 7px; }
  .social-marker { width: 9px; height: 9px; background: var(--brand-blue); border-radius: 50%; }
  .edge-tab {
    position: absolute; right: -8px; top: 215px; width: 18px; height: 32px;
    background: var(--brand-blue); border-radius: 6px;
  }
  .footer-band { position: absolute; left: 0; bottom: 0; width: 760px; height: 13px; }
</style>
</head>
<body>
<main class="stage">
  <section class="card-front" aria-label="Card front">
    <div class="front-wordmark">Brava Set</div>
    <div class="front-url">www.Brava<span class="accent">Set</span>-example.com</div>
  </section>

  <section class="card-back" aria-label="Card back">
    <div class="back-wordmark">Brava Set</div>

    <div class="holder">
      <div class="holder-name">Peter Halvik</div>
      <div class="holder-title">CEO / Co-Owner</div>
    </div>
    <div class="edge-tab"></div>

    <div class="divider"></div>

    <ul class="contact-list">
      <li><svg viewBox="0 0 16 16"><path d="M3 1l3 3-1.5 2c1 2 3 4 5 5l2-1.5 3 3-2 2C6 14 2 10 1 3z"/></svg><span>555.210.4873</span></li>
      <li><svg viewBox="0 0 16 16"><path d="M4 1h8v4H4zM1 6h14v6h-3v3H4v-3H1zM5 10v4h6v-4z"/></svg><span>555.210.6692</span></li>
      <li><svg viewBox="0 0 16 16"><path d="M1 3h14v1L8 9 1 4zM1 6l7 5 7-5v7H1z"/></svg><span>peter@bravaset-example.com</span></li>
      <li><svg viewBox="0 0 16 16"><path d="M8 1a7 7 0 100 14A7 7 0 008 1zm0 1.5c.8 0 1.8 2 2 4.5H6c.2-2.5 1.2-4.5 2-4.5zM2.6 7h2A11 11 0 015.5 3 5.5 5.5 0 002.6 7zm8.8 0h2a5.5 5.5 0 00-2.9-4 11 11 0 01.9 4zM2.6 9a5.5 5.5 0 002.9 4 11 11 0 01-.9-4zm3.4 0c.2 2.5 1.2 4.5 2 4.5s1.8-2 2-4.5zm5.4 0a11 11 0 01-.9 4 5.5 5.5 0 002.9-4z"/></svg><span>www.Brava<span class="accent">Set</span>-example.com</span></li>
    </ul>

    <address class="address">
      418 Corvell Avenue,<br>
      Unit 9 North Hollywood,<br>
      California 91602
    </address>

    <div class="social">
      <span><i class="social-marker"></i>/bravasetny</span>
      <span><i class="social-marker"></i>brava_set</span>
    </div>

    <svg class="footer-band" viewBox="0 0 760 13" preserveAspectRatio="none" aria-hidden="true">
      <polygon points="0,0 470,0 462,13 0,13" fill="var(--brand-black)"/>
      <polygon points="476,0 760,0 760,13 468,13" fill="var(--brand-blue)"/>
    </svg>
  </section>
</main>
</body>
</html>
```